Harbourline Refrigeration business card design

We would like a new design for our business card as we have a new logo.
We need generic business card to give our customers with our office details - with the option of making it individualized for each manager

Target Market(s)

Companies and homeowners

Industry/Entity Type

Air Conditioning

Contact Information for Business Card

We are not sure if we want single or double sided it will depend on the design we choose

Colors
33a6d7
0255a3

Requirements
Must have
• Logo
• phone: (08) 8721 5940
• email: harbourserve@tealnet.example
• website: www.harbourlinerefrigeration.example
• AU61420
• BLD472913
Nice to have
• Address - Shed 5/284 Tallis Rd, Marlow Bay SA 5710

```html
<!DOCTYPE html>
<html lang="en">
<head>
<meta charset="utf-8">
<title>Harbourline Refrigeration – Business Card</title>
<link href="https://fonts.googleapis.com/css2?family=Montserrat:wght@500;700&family=Roboto+Condensed:wght@400&display=swap" rel="stylesheet">
<style>
  :root {
    --backdrop: #e4e6ea;
    --card-blue: #1d4f8c;
    --card-blue-deep: #174478;
    --ink-white: #ffffff;
    --ink-soft: rgba(255,255,255,0.86);
    --accent-sky: #33a6d7;
  }
  * { box-sizing: border-box; margin: 0; padding: 0; }
  html, body {
    width: 1200px; height: 800px; overflow: hidden;
    background: var(--backdrop);
    font-family: "Montserrat", sans-serif;
  }
  .sheet {
    width: 1200px; height: 800px;
    display: flex; align-items: center; justify-content: center; gap: 60px;
  }
  .card {
    width: 510px; height: 312px;
    border-radius: 14px;
    background: linear-gradient(150deg, var(--card-blue) 0%, var(--card-blue-deep) 100%);
    color: var(--ink-white);
    position: relative;
    box-shadow: 0 6px 18px rgba(20,40,80,0.18);
  }
  /* Front: brand side */
  .card--front {
    display: flex; flex-direction: column; align-items: center; justify-content: center;
  }
  .brand { display: flex; align-items: center; gap: 14px; }
  .brand__name {
    font-weight: 700; font-size: 54px; letter-spacing: -0.5px; line-height: 1;
  }
  .brand__dot {
    width: 26px; height: 26px; border-radius: 50%;
    background: var(--ink-white);
  }
  .brand__tagline {
    font-family: "Roboto Condensed", sans-serif;
    font-size: 14px; letter-spacing: 1.6px; text-transform: uppercase;
    margin-top: 8px;
  }
  .card--front .website {
    font-size: 12px; margin-top: 22px; color: var(--ink-soft);
  }
  /* Back: contact side */
  .card--back { padding: 34px 38px; }
  .brand--small .brand__name { font-size: 28px; }
  .brand--small .brand__dot { width: 14px; height: 14px; }
  .card--back .brand__tagline { font-size: 8.5px; letter-spacing: 1px; margin-top: 4px; }
  .person { margin-top: 24px; }
  .person__name {
    font-weight: 700; font-size: 20px; letter-spacing: 1px; text-transform: uppercase;
  }
  .person__role { font-size: 12px; font-weight: 500; margin-top: 3px; }
  .contacts { list-style: none; margin-top: 18px; font-size: 12px; font-weight: 500; }
  .contacts li { display: flex; align-items: center; gap: 8px; line-height: 1.65; }
  .contacts svg { width: 11px; height: 11px; flex: none; }
  .contacts .plain { padding-left: 19px; }
  .address { margin-top: 10px; font-size: 12px; font-weight: 500; line-height: 1.6; }
</style>
</head>
<body>
<main class="sheet">
  <section class="card card--front" aria-label="Card front">
    <div class="brand">
      <span class="brand__name">Harbourline</span>
      <span class="brand__dot"></span>
    </div>
    <p class="brand__tagline">Refrigeration &amp; Air Conditioning</p>
    <p class="website">www.harbourlinerefrigeration.example</p>
  </section>

  <section class="card card--back" aria-label="Card back">
    <div class="brand brand--small">
      <span class="brand__name">Harbourline</span>
      <span class="brand__dot"></span>
    </div>
    <p class="brand__tagline">Refrigeration &amp; Air Conditioning</p>

    <div class="person">
      <p class="person__name">Dana Whitlock</p>
      <p class="person__role">CEO/Founder</p>
    </div>

    <ul class="contacts">
      <li>
        <svg viewBox="0 0 24 24" aria-hidden="true"><path fill="#fff" d="M6.6 10.8a15 15 0 0 0 6.6 6.6l2.2-2.2c.3-.3.7-.4 1-.2 1.1.4 2.3.6 3.6.6.6 0 1 .4 1 1V20c0 .6-.4 1-1 1A17 17 0 0 1 3 4c0-.6.4-1 1-1h3.5c.6 0 1 .4 1 1 0 1.3.2 2.5.6 3.6.1.3 0 .7-.2 1z"/></svg>
        (08) 8721 5940
      </li>
      <li>
        <svg viewBox="0 0 24 24" aria-hidden="true"><rect x="2" y="5" width="20" height="14" rx="2" fill="none" stroke="#fff" stroke-width="2"/><path d="M2 6l10 7 10-7" fill="none" stroke="#fff" stroke-width="2"/></svg>
        harbourserve@tealnet.example
      </li>
      <li>
        <svg viewBox="0 0 24 24" aria-hidden="true"><circle cx="12" cy="12" r="9.5" fill="none" stroke="#fff" stroke-width="2"/><path d="M2.5 12h19M12 2.5c3 3 3 16 0 19M12 2.5c-3 3-3 16 0 19" fill="none" stroke="#fff" stroke-width="1.6"/></svg>
        www.harbourlinerefrigeration.example
      </li>
      <li class="plain">AU61420, BLD472913</li>
    </ul>

    <p class="address">Shed 5/284 Tallis Rd<br>Marlow Bay SA 5710</p>
  </section>
</main>
</body>
</html>
```